Crestwell Grand Piano Academy is a comprehensive piano studio located in CBD area and provide individual piano lessons.

We also provide services for wedding organising band, or instrumental hiring or venue hiring, or organise concert to students.

I want my name card to be very creative, does not have to be the form or shape with the normal name card, can be in different shape. Also, I want the name card to be very upper class, because learning piano is a serious thing, so I do not want people to bargain with the prices. I want people to see it as a very elegant tuition so that they do not want to bargain and think it is worth to try.

Further more, Crestwell Grand Piano Academy is not like normal piano studio only provide piano lessons, we provide band services for each other event, such as cruise party, wedding etc. I want people to see it as owner of Grand Piano Academy, they will have different type of services all in one, I provide more than that, and I am well connected. I do not provide only piano lesson, but also all other musical knowledge and I am very professional

I want name card to be very simple, just name of company name, my name and website that's all, maybe phone number and email as well.

Please check my website to have more ideal concept.
http://dorvanpeq.sitebuild.example/crestwellpianoacademy

Target Market(s)

For all people who love to play piano (better with upper class)

Industry/Entity Type

Wedding

Contact Information for Business Card

Clara Voss
Mobile:0419876502
Email: crestwellgrandstudio@mailbrook.example

Colors

Designer to choose colors to be used in the design.

Requirements
Must have
• Creativity
Nice to have
• Black and white
some sort of piano image
Should not have
• Childish

```html
<!DOCTYPE html>
<html lang="en">
<head>
<meta charset="UTF-8">
<title>Crestwell Grand Piano Academy – Business Cards</title>
<link href="https://fonts.googleapis.com/css2?family=Roboto:wght@100;300;400;700&display=swap" rel="stylesheet">
<style>
  :root {
    --ink: #231f20;
    --paper: #ffffff;
    --backdrop: #e8e5e0;
    --muted: #9a9a9a;
  }
  * { margin: 0; padding: 0; box-sizing: border-box; }
  html, body { width: 1200px; height: 750px; overflow: hidden; }
  body {
    background: var(--backdrop);
    font-family: "Roboto", Helvetica, Arial, sans-serif;
    position: relative;
  }
  .card {
    position: absolute;
    width: 356px;
    height: 206px;
  }
  .card > svg { position: absolute; inset: 0; }
  .card--front-dark  { left: 220px; top: 92px; }
  .card--back-light  { left: 596px; top: 92px; }
  .card--front-light { left: 220px; top: 406px; }
  .card--back-dark   { left: 596px; top: 406px; }

  .fill-ink { fill: var(--ink); }
  .fill-paper { fill: var(--paper); }

  .brand {
    position: absolute;
    left: 70px;
    top: 78px;
    text-transform: uppercase;
    font-weight: 700;
    line-height: 1;
  }
  .brand__line1 { display: block; font-size: 19px; letter-spacing: 4.2px; }
  .brand__line2 { display: block; font-size: 24.5px; letter-spacing: 0.3px; margin-top: 5px; }

  .person {
    position: absolute;
    right: 122px;
    top: 14px;
    text-align: right;
  }
  .person__name { font-size: 21px; font-weight: 100; letter-spacing: 0.2px; line-height: 1.1; }
  .person__role { font-size: 6.5px; font-weight: 300; letter-spacing: 0.5px; text-transform: uppercase; color: var(--muted); line-height: 1; }

  .contact {
    position: absolute;
    left: 92px;
    top: 82px;
    list-style: none;
  }
  .contact::after {
    content: "";
    position: absolute;
    left: 22px;
    top: -2px;
    height: 66px;
    border-left: 1px solid currentColor;
  }
  .contact__item {
    display: flex;
    align-items: center;
    height: 21px;
    font-size: 9.5px;
    font-weight: 400;
  }
  .contact__icon { width: 12px; height: 12px; margin-right: 18px; flex: none; }

  .on-dark { color: var(--paper); }
  .on-light { color: var(--ink); }
</style>
</head>
<body>

<svg width="0" height="0" style="position:absolute">
  <defs>
    <clipPath id="card-shape">
      <polygon points="22,0 356,0 356,184 334,206 0,206 0,22"/>
    </clipPath>
    <symbol id="icon-phone" viewBox="0 0 12 12">
      <rect x="3" y="0.5" width="6" height="11" rx="1" fill="currentColor"/>
      <rect x="4" y="2" width="4" height="3" fill="var(--paper)"/>
      <rect x="4" y="6" width="4" height="4" fill="var(--paper)" opacity="0.6"/>
    </symbol>
    <symbol id="icon-mail" viewBox="0 0 12 12">
      <rect x="0.5" y="2.5" width="11" height="7" fill="none" stroke="currentColor" stroke-width="1"/>
      <polyline points="0.5,2.5 6,7 11.5,2.5" fill="none" stroke="currentColor" stroke-width="1"/>
    </symbol>
    <symbol id="icon-web" viewBox="0 0 12 12">
      <circle cx="6" cy="6" r="5.2" fill="none" stroke="currentColor" stroke-width="1"/>
      <ellipse cx="6" cy="6" rx="2.3" ry="5.2" fill="none" stroke="currentColor" stroke-width="0.9"/>
      <line x1="0.8" y1="6" x2="11.2" y2="6" stroke="currentColor" stroke-width="0.9"/>
    </symbol>
  </defs>
</svg>

<!-- Front, dark -->
<div class="card card--front-dark on-dark">
  <svg width="356" height="206" viewBox="0 0 356 206">
    <g clip-path="url(#card-shape)">
      <rect class="fill-ink" width="356" height="206"/>
      <polygon class="fill-paper" points="311,0 356,0 356,43"/>
      <polygon class="fill-paper" points="0,160 45,206 0,206"/>
    </g>
  </svg>
  <h1 class="brand">
    <span class="brand__line1">Crestwell Grand</span>
    <span class="brand__line2">Piano Academy</span>
  </h1>
</div>

<!-- Back, light -->
<div class="card card--back-light on-light">
  <svg width="356" height="206" viewBox="0 0 356 206">
    <g clip-path="url(#card-shape)">
      <rect class="fill-paper" width="356" height="206"/>
      <polygon class="fill-ink" points="0,30 160,206 0,206"/>
      <polygon class="fill-ink" points="356,161 356,206 312,206"/>
    </g>
  </svg>
  <div class="person">
    <p class="person__name">Marten Okoro</p>
    <p class="person__role">Designer</p>
  </div>
  <ul class="contact">
    <li class="contact__item"><svg class="contact__icon"><use href="#icon-phone"/></svg>0419876502</li>
    <li class="contact__item"><svg class="contact__icon"><use href="#icon-mail"/></svg>crestwellgrandstudio@mailbrook.example</li>
    <li class="contact__item"><svg class="contact__icon"><use href="#icon-web"/></svg>dorvanpeq.sitebuild.example/crestwellpianoacademy</li>
  </ul>
</div>

<!-- Front, light -->
<div class="card card--front-light on-light">
  <svg width="356" height="206" viewBox="0 0 356 206">
    <g clip-path="url(#card-shape)">
      <rect class="fill-paper" width="356" height="206"/>
      <polygon class="fill-ink" points="311,0 356,0 356,43"/>
      <polygon class="fill-ink" points="0,160 45,206 0,206"/>
    </g>
  </svg>
  <h1 class="brand">
    <span class="brand__line1">Crestwell Grand</span>
    <span class="brand__line2">Piano Academy</span>
  </h1>
</div>

<!-- Back, dark -->
<div class="card card--back-dark on-dark">
  <svg width="356" height="206" viewBox="0 0 356 206">
    <g clip-path="url(#card-shape)">
      <rect class="fill-ink" width="356" height="206"/>
      <polygon class="fill-paper" points="0,30 160,206 0,206"/>
      <polygon class="fill-paper" points="356,161 356,206 312,206"/>
    </g>
  </svg>
  <div class="person">
    <p class="person__name">Marten Okoro</p>
    <p class="person__role">Designer</p>
  </div>
  <ul class="contact">
    <li class="contact__item"><svg class="contact__icon" style="--paper:#231f20"><use href="#icon-phone"/></svg>0419876502</li>
    <li class="contact__item"><svg class="contact__icon"><use href="#icon-mail"/></svg>crestwellgrandstudio@mailbrook.example</li>
    <li class="contact__item"><svg class="contact__icon"><use href="#icon-web"/></svg>dorvanpeq.sitebuild.example/crestwellpianoacademy</li>
  </ul>
</div>

</body>
</html>
```